Higher $ Now Guaranteed! Redesign Web Page(s) Style Composition and Color (Graphics design-not code)

We need a modern look for an existing website. You can either use or change the current logo. Choice of colors, fonts, style is up to you. Sample URLs and additional details are provided in the attached document. Most of our struggle has been the appearance of the directory listings (city) page.
----------------------------------------------------------------------------------
--> Increased Project Budget and Now Funds are GUARANTEED
--> Added an additional attachment in response to questions
-->THIS PROJECT IS FOR GRAPHICS/DESIGN NOT CODE
The project is mostly a few areas of text and colored boxes or lines. Hopefully a skilled designer can place these elements in an attractive layout and choose the right colors and styles. There are no complex drawings required for this project.

*** We are involved with other projects from time to time and expect that the winning designer will be given the first opportunity at this future work. ***

*** There is no requirement to do any code but if you submit a design feel free to indicate if you wish to be considered for any future code work on this site or others ***

Font styles to use
Sans Serif

Requirements
Must have
• Rounded corners on images and buttons with nice gradients or hover effects.
Nice to have
• Attached an additional descriptions document to help with these answers.
Should not have
• Small fonts, traditional older looking rectangular buttons, dull or boring color schemes

```html
<!DOCTYPE html>
<html lang="en">
<head>
<meta charset="utf-8">
<title>TaxFinder Hub</title>
<link rel="stylesheet" href="https://fonts.googleapis.com/css2?family=Roboto:wght@300;400;500;700&family=Roboto+Condensed:wght@400;700&family=Jost:wght@400;500&display=swap">
<style>
:root{
  --yellow:#fcd21c;
  --blue:#00a8f0;
  --blue-light:#5ab9f3;
  --blue-field:#2fa0ea;
  --dark:#333436;
  --darker:#222325;
  --ink:#1f1f1f;
  --white:#ffffff;
  --logo-blue:#1e9be0;
  --muted:#555555;
}
*{box-sizing:border-box;margin:0;padding:0}
html,body{width:1200px;height:904px;overflow:hidden;background:var(--white)}
body{position:relative;font-family:"Roboto",Arial,sans-serif;color:var(--ink)}
.abs{position:absolute}

/* header */
.site-header{left:0;top:0;width:1200px;height:113px;background:var(--white)}
.brand{left:252px;top:44px;font:400 38px/1 "Roboto",sans-serif;color:var(--logo-blue);display:flex;align-items:center;gap:10px;letter-spacing:-.5px}
.brand-dot{width:22px;height:22px;border-radius:50%;background:var(--yellow)}
.contact-line{left:688px;top:14px;display:flex;align-items:center;gap:10px;font:700 13px "Roboto Condensed",sans-serif}
.phone-icon{width:18px;height:18px;border-radius:50%;background:var(--yellow);display:flex;align-items:center;justify-content:center}
.touch{margin-left:20px}
.social{width:24px;height:24px;border-radius:50%;display:inline-block}
.social.one{background:#1c3f94}.social.two{background:#27a9e6}
.search-bar{left:675px;top:63px;display:flex;gap:6px}
.search-bar input{width:118px;height:20px;border:1px solid #d6d6d6;border-radius:2px;font:400 8px "Roboto Condensed",sans-serif;padding-left:8px;color:var(--muted)}
.search-btn{width:27px;height:20px;background:var(--blue);border-radius:3px;display:flex;align-items:center;justify-content:center;margin-left:1px}

/* nav */
.main-nav{left:0;top:113px;width:1200px;height:34px;background:var(--yellow)}
.main-nav ul{list-style:none;display:flex;position:absolute;left:231px;top:0;height:34px}
.main-nav li{font:300 14px/34px "Roboto",sans-serif;color:#333;padding:0 26px}
.main-nav li.active{background:var(--dark);color:var(--white)}

/* hero */
.hero{left:0;top:147px;width:1200px;height:370px;background:var(--dark)}
.map-panel{left:240px;top:29px;width:436px;height:316px;background:var(--blue);border:4px solid #bfe6fb;border-radius:14px;text-align:center;color:var(--white)}
.map-panel h1{font:700 23px "Roboto Condensed",sans-serif;margin-top:10px;letter-spacing:.2px}
.map-panel p{font:400 10px "Roboto",sans-serif;margin-top:3px}
.map-area{position:absolute;left:30px;top:72px;width:372px;height:216px;border-radius:10px;background:linear-gradient(135deg,#9ad97e 0%,#f4dc5a 45%,#f2ae5a 75%,#8fd3f6 100%);opacity:.85}
.search-panel{left:684px;top:29px;width:262px;height:316px;background:var(--blue-light);border:4px solid #e6f3fc;border-radius:14px;overflow:hidden}
.search-strip{position:absolute;left:0;top:0;width:46px;height:100%;background:#dcebf7;border-right:3px solid #e6f3fc}
.search-strip span{position:absolute;left:50%;top:50%;transform:translate(-50%,-50%) rotate(-90deg);white-space:nowrap;font:700 20px "Roboto Condensed",sans-serif;color:#222}
.field-label{position:absolute;left:62px;font:500 10px "Roboto",sans-serif;color:var(--white)}
.field{position:absolute;left:57px;width:190px;height:28px;background:var(--blue-field);border-radius:4px}
.search-submit{position:absolute;left:78px;top:261px;width:151px;height:29px;background:linear-gradient(#eef5fb,#d6e7f5);border-radius:5px;font:400 11px/29px "Roboto Condensed",sans-serif;text-align:center;color:#222}

/* promos */
.promo{top:517px;height:237px;overflow:hidden}
.promo-find{left:0;width:606px;background:var(--blue);color:var(--white)}
.promo-join{left:606px;width:594px;background:var(--yellow);color:var(--ink)}
.promo-photo{position:absolute;top:0;height:237px}
.promo-find .promo-photo{left:0;width:238px;background:linear-gradient(90deg,#7a5a46 0%,#b98a6c 55%,rgba(0,168,240,0) 100%)}
.promo-join .promo-photo{right:0;width:246px;background:linear-gradient(270deg,#9b6a4d 0%,#e6c2a6 60%,rgba(252,210,28,0) 100%)}
.promo-title{position:absolute;top:15px;font:400 30px/1.05 "Jost",sans-serif}
.promo-title strong{display:block;font-weight:500;font-size:32px;letter-spacing:.3px}
.promo-text{position:absolute;top:91px;width:340px;font:400 13px/19px "Roboto",sans-serif}
.promo-btn{position:absolute;top:174px;width:145px;height:36px;font:500 12px/34px "Roboto Condensed",sans-serif;text-align:center;letter-spacing:.3px;border-radius:6px}
.promo-find .promo-title,.promo-find .promo-text,.promo-find .promo-btn{left:239px}
.promo-find .promo-btn{border:1px solid var(--white);color:var(--white);background:linear-gradient(rgba(255,255,255,.12),rgba(255,255,255,0))}
.promo-join .promo-title,.promo-join .promo-text,.promo-join .promo-btn{left:14px}
.promo-join .promo-btn{border:1px solid var(--ink);color:var(--ink);background:linear-gradient(rgba(255,255,255,.25),rgba(255,255,255,0))}

/* footer */
.site-footer{left:0;top:754px;width:1200px;height:99px;background:var(--white)}
.foot-col{position:absolute;top:20px}
.foot-col h3{font:700 10px "Roboto Condensed",sans-serif;margin-bottom:5px}
.foot-col li{list-style:none;font:400 8px/15px "Roboto",sans-serif;color:var(--muted)}
.foot-brand{left:698px;top:34px;font-size:33px}
.bottom-bar{left:0;top:853px;width:1200px;height:51px;background:var(--darker);color:var(--white);font:400 8px "Roboto Condensed",sans-serif}
.copyright{position:absolute;left:240px;top:21px}
.bottom-social{position:absolute;left:834px;top:14px;display:flex;align-items:center;gap:8px}
.bottom-social .social{width:18px;height:18px}
</style>
</head>
<body>

<header class="site-header abs">
  <div class="brand abs"><span class="brand-dot"></span>TaxFinder Hub</div>
  <div class="contact-line abs">
    <span class="phone-icon"><svg width="10" height="10" viewBox="0 0 24 24"><path fill="#333" d="M6.6 10.8a15 15 0 006.6 6.6l2.2-2.2a1 1 0 011-.25 11.4 11.4 0 003.6.57 1 1 0 011 1V20a1 1 0 01-1 1A17 17 0 013 4a1 1 0 011-1h3.5a1 1 0 011 1c0 1.25.2 2.45.57 3.57a1 1 0 01-.25 1z"/></svg></span>
    <span>555-014-2290</span>
    <span class="touch">Get in touch with us</span>
    <span class="social one"></span><span class="social two"></span>
  </div>
  <form class="search-bar abs">
    <input type="text" placeholder="Enter a keyword or name">
    <input type="text" placeholder="Enter a location">
    <span class="search-btn"><svg width="12" height="12" viewBox="0 0 24 24"><circle cx="10" cy="10" r="6" fill="none" stroke="#fff" stroke-width="3"/><path d="M14.5 14.5L20 20" stroke="#fff" stroke-width="3" stroke-linecap="round"/></svg></span>
  </form>
</header>

<nav class="main-nav abs">
  <ul>
    <li class="active">Home</li>
    <li>Get Listed</li>
    <li>How It Works</li>
    <li>Join Today</li>
    <li>Directory Search</li>
    <li>Contact Us</li>
  </ul>
</nav>

<section class="hero abs">
  <div class="map-panel abs">
    <h1>FIND LOCAL TAX PROFESSIONALS</h1>
    <p>To search just click on the map on our desired location</p>
    <div class="map-area" role="img" aria-label="Clickable map of the United States with colored states"></div>
  </div>
  <div class="search-panel abs">
    <div class="search-strip"><span>ADVANCED SEARCH</span></div>
    <span class="field-label" style="top:42px">Type your state</span>
    <span class="field" style="top:62px"></span>
    <span class="field-label" style="top:109px">Type your city</span>
    <span class="field" style="top:129px"></span>
    <span class="field-label" style="top:176px">Type zip</span>
    <span class="field" style="top:196px"></span>
    <span class="search-submit">SEARCH</span>
  </div>
</section>

<section class="promo promo-find abs">
  <div class="promo-photo" role="img" aria-label="Photo of a smiling young man"></div>
  <h2 class="promo-title">Find The Best<strong>TAX PROFESSIONALS</strong></h2>
  <p class="promo-text">Our directories of tax professionals give you immediate access to the very best tax preparers and income tax advisors in your area.</p>
  <span class="promo-btn">GET STARTED</span>
</section>

<section class="promo promo-join abs">
  <div class="promo-photo" role="img" aria-label="Photo of a smiling young woman"></div>
  <h2 class="promo-title">Are You A<strong>TAX PREPARER?</strong></h2>
  <p class="promo-text">Our directories give tax preparers access to new clients and prospects looking for income tax return preparation and other tax services in your local area.</p>
  <span class="promo-btn">SUBMIT LISTING</span>
</section>

<footer class="site-footer abs">
  <div class="foot-col" style="left:244px"><h3>NAVIGATION</h3><ul><li>Directory</li><li>Special Offers</li><li>Contact Us</li></ul></div>
  <div class="foot-col" style="left:382px"><h3>CONTACT</h3><ul><li>PO Box 4410</li><li>Millbrook, CT</li><li>06000</li></ul></div>
  <div class="foot-col" style="left:510px"><h3>LEGAL</h3><ul><li>Terms &amp; Condition</li><li>Packages</li><li>FAQ</li></ul></div>
  <div class="brand foot-brand abs"><span class="brand-dot"></span>TaxFinder Hub</div>
</footer>

<div class="bottom-bar abs">
  <span class="copyright">©2015, All Rights Reserved, TaxFinderHub.example</span>
  <span class="bottom-social">Get in touch with us <span class="social one"></span><span class="social two"></span></span>
</div>

</body>
</html>
```